Buttons, Banners & MPUs - 'Coastal Getaway Digest'

We are launching a new product - a bookazine on sale later this month!

General description below:

COASTAL GETAWAY DIGESTS 2015

Calling all lovers of French holidays! Where will you go in 2015?

Let us guide you to the very best holidays in France with our brand new guide, featuring 180 pages of high quality and inspiring editorial and imagery. Coastal Getaways Digests 2015 provides a comprehensive, ideas-packed guide to classic breaks, as well as niche and new holiday ideas across France.

Love to get out in the French fresh air? We have activities such as boating, cycling and golf covered. There’s plenty for culture vultures and city breakers, too, plus lots of great ideas for family breaks including theme parks, zoos and attractions.

We whet the appetite of foodies and wine lovers, provide a guide to markets and festivals and also get off the beaten track with guides to driving, railway holidays and visit some of France’s most beautiful villages. And if you want to get creative, there are loads of ideas for photography, art, ‘me time’ escapes and tempting snapshots of some of France’s most unusual accommodation.

Whatever you love about France, there’s a fabulous French holiday made for you!

Design brief - bright, fun, exciting, inspiring.. with a clear call-to-action

We require a variety of sizes including:
300 x 250, 250 x 250, 728 x 90, 468 x 60, 120 x 600, 120 x 240, 600 x 200
- please only create a couple to showcase your design

More information can be found on the products website but please be aware that this is still under construction so please do not base your design on this: http://www.coastalgetawaydigests.example/

Target Market(s)

Francophiles, holiday makers, 40+, families, couples,

Industry/Entity Type

Construction

Font styles to use
Serif
Sans Serif

Requirements
Must have
• Logo
• Call to action
Nice to have
• Suggested strap lines:
• - The ultimate guide to holidays in France
• - The biggest and best guide to France
• - 180 pages of Fabulous French Holiday Ideas
• - What's New in 2015
Should not have
• Price - we want to direct traffic to our website which will reflect their local currency

```html
<!DOCTYPE html>
<html lang="en">
<head>
<meta charset="utf-8">
<title>Coastal Getaway Digest 2015 – Banner Set</title>
<link rel="stylesheet" href="https://fonts.googleapis.com/css2?family=Arimo:wght@400;700&family=Open+Sans:wght@600;700&display=swap">
<style>
  :root{
    --navy:#28287f;
    --navy-dark:#1d1d63;
    --red:#e3181f;
    --white:#ffffff;
    --stage:#ece8e2;
    --rule:#b9b9c2;
    --sky-top:#4f9fe0;
    --sky-bottom:#cfe6f5;
    --snow-top:#7fb4e6;
    --snow-bottom:#eef5fb;
    --beach-top:#8fc7ea;
    --beach-bottom:#e7d7b8;
  }
  *{box-sizing:border-box;margin:0;padding:0}
  html,body{width:1200px;height:900px;overflow:hidden}
  body{background:var(--stage);position:relative;font-family:"Arimo",Arial,sans-serif;color:var(--navy)}

  .banner{position:absolute;background:var(--white);box-shadow:0 2px 6px rgba(0,0,0,.18)}
  .brand{font-family:"Arimo",Arial,sans-serif;font-weight:700;color:var(--navy);text-align:center;line-height:1.02;letter-spacing:-.5px}
  .headline{font-weight:700;color:var(--navy);text-align:center;line-height:1.18}
  .headline .accent{color:var(--red)}
  .photo{position:absolute;border:3px solid var(--navy);border-radius:5px}
  .photo--city{background:linear-gradient(180deg,var(--sky-top),var(--sky-bottom) 70%,#6f8fa0)}
  .photo--snow{background:linear-gradient(200deg,var(--snow-top),var(--snow-bottom) 65%)}
  .photo--beach{background:linear-gradient(180deg,var(--beach-top),#bfe0ef 45%,var(--beach-bottom))}
  .cta{position:absolute;display:flex;align-items:center;justify-content:center;
       background:linear-gradient(180deg,#4a4aa0,var(--navy-dark));color:var(--white);
       font-family:"Open Sans",Arial,sans-serif;font-weight:700;font-size:17px;border-radius:4px;
       box-shadow:0 2px 3px rgba(0,0,0,.35);text-decoration:none}
  .url{position:absolute;left:0;right:0;text-align:center;font-family:"Open Sans",Arial,sans-serif;font-weight:600;font-size:13px;color:var(--navy)}
  .brand-rule{position:absolute;left:0;right:0;height:5px;background:linear-gradient(180deg,var(--rule),#eee)}

  /* 728 x 90 leaderboard */
  .leaderboard{left:185px;top:43px;width:853px;height:106px}
  .leaderboard .headline{position:absolute;left:8px;top:12px;width:392px;font-size:30px}
  .leaderboard .photo{left:420px;top:5px;width:173px;height:95px}
  .leaderboard .divider{position:absolute;left:620px;top:0;width:5px;height:106px;background:linear-gradient(90deg,#888,#ddd)}
  .leaderboard .brand{position:absolute;left:632px;top:4px;width:215px;font-size:18px}
  .leaderboard .cta{left:656px;top:46px;width:168px;height:37px}
  .leaderboard .url{left:625px;top:87px}

  /* 300 x 250 MPU */
  .mpu{left:318px;top:325px;width:394px;height:328px}
  .mpu .brand{position:absolute;left:0;right:0;top:8px;font-size:32px}
  .mpu .brand-rule{top:82px}
  .mpu .headline{position:absolute;left:0;right:0;top:93px;font-size:30px}
  .mpu .photo--city{left:16px;top:167px;width:172px;height:94px}
  .mpu .photo--snow{left:203px;top:167px;width:173px;height:94px}
  .mpu .cta{left:112px;top:270px;width:168px;height:38px}
  .mpu .url{top:307px}

  /* 120 x 600 skyscraper */
  .skyscraper{left:761px;top:175px;width:187px;height:702px}
  .skyscraper .brand{position:absolute;left:0;right:0;top:22px;font-size:22px}
  .skyscraper .brand-rule{top:86px}
  .skyscraper .headline{position:absolute;left:0;right:0;top:98px}
  .skyscraper .headline > .line{display:block}
  .skyscraper .small{font-size:23px;font-weight:400;line-height:1.1}
  .skyscraper .big{font-size:35px;color:var(--red);line-height:1.1}
  .skyscraper .mid{font-size:33px;line-height:1.12}
  .skyscraper .mid .plain{font-size:23px;font-weight:400;color:var(--navy)}
  .skyscraper .photo{left:7px;width:172px;height:94px}
  .skyscraper .photo--city{top:278px}
  .skyscraper .photo--snow{top:387px}
  .skyscraper .photo--beach{top:496px}
  .skyscraper .cta{left:8px;top:616px;width:170px;height:37px}
  .skyscraper .url{top:657px;font-size:12.5px}
</style>
</head>
<body>

<section class="banner leaderboard" aria-label="Leaderboard banner">
  <h2 class="headline">The <span class="accent">BIGGEST</span> and <span class="accent">BEST</span><br>Guide to <span class="accent">FRANCE</span></h2>
  <div class="photo photo--city" role="img" aria-label="River cruise boat on the Seine with the Eiffel Tower behind"></div>
  <div class="divider"></div>
  <div class="brand">Coastal Getaway<br>Digest 2015</div>
  <a class="cta" href="#">FIND OUT MORE</a>
  <p class="url">coastalgetawaydigests.example</p>
</section>

<section class="banner mpu" aria-label="MPU banner">
  <div class="brand">Coastal Getaway<br>Digest 2015</div>
  <div class="brand-rule"></div>
  <h2 class="headline">The <span class="accent">BIGGEST</span> and <span class="accent">BEST</span><br>Guide to <span class="accent">FRANCE</span></h2>
  <div class="photo photo--city" role="img" aria-label="River cruise boat on the Seine with the Eiffel Tower behind"></div>
  <div class="photo photo--snow" role="img" aria-label="Skier on a chairlift above snowy mountains"></div>
  <a class="cta" href="#">FIND OUT MORE</a>
  <p class="url">coastalgetawaydigests.example</p>
</section>

<section class="banner skyscraper" aria-label="Skyscraper banner">
  <div class="brand">Coastal Getaway<br>Digest 2015</div>
  <div class="brand-rule"></div>
  <h2 class="headline">
    <span class="line small">The</span>
    <span class="line big">BIGGEST</span>
    <span class="line mid"><span class="plain">and </span><span class="accent">BEST</span></span>
    <span class="line small">Guide to</span>
    <span class="line big">FRANCE</span>
  </h2>
  <div class="photo photo--city" role="img" aria-label="River cruise boat on the Seine with the Eiffel Tower behind"></div>
  <div class="photo photo--snow" role="img" aria-label="Skier on a chairlift above snowy mountains"></div>
  <div class="photo photo--beach" role="img" aria-label="Children with beach inflatables walking toward the sea"></div>
  <a class="cta" href="#">FIND OUT MORE</a>
  <p class="url">coastalgetawaydigests.example</p>
</section>

</body>
</html>
```